Update our insurance company Business Card

Create a more current card with two locations. Northgate & Pine Harbor. Please make suggestions for: photo or no photos, back of card, type of material etc. We are risk advisors / insurance brokers and cater to businesses and the affluent home owner. We have been in a luxury resort community for 8 years and are expanding to a second location in Northgate.

Target Market(s)

We are risk advisors / insurance brokers and cater to businesses (Tech, Healthcare, Restaurants, Hotels, Commercial property) and the affluent home owner. We have been in a luxury resort community for 8 years and are expanding to a second location in Northgate.

Industry/Entity Type

Insurance

Contact Information for Business Card

Tavish K. Merriam, CLCS
President & CEO

Pine Harbor: 555-014-2267
Northgate: TBD
Fax: 555-014-2268
E-Mail: Tavish@mwcoverageteam.com

Website: www.mwcoverageteam.com

Colors

Designer to choose colors to be used in the design.

Requirements
Must have
• LOGO. I will need phone #'s for Northgate, Pine Harbor, Mobile, and Fax. Website and e-mail. Must have cropped photo chest up or face.
Nice to have
• Please make suggestions for: QR Code or something better, photo, back of card, type of material etc. Red edging. See file.

```html
<!DOCTYPE html>
<html lang="en">
<head>
<meta charset="utf-8">
<title>MW Coverage Team – Business Card</title>
<link rel="stylesheet" href="https://fonts.googleapis.com/css2?family=Cinzel:wght@400;700&family=Open+Sans:wght@400&family=Oswald:wght@400&display=swap">
<style>
  :root {
    --backdrop: #e9e6e2;
    --ink: #0b0b0b;
    --paper: #ffffff;
    --accent: #e2231a;
    --text-light: #f4f4f4;
    --photo-dark: #2b2f3a;
    --photo-mid: #7a6a5c;
  }
  * { margin: 0; padding: 0; box-sizing: border-box; }
  html, body { width: 1200px; height: 1000px; overflow: hidden; background: var(--backdrop); }
  .canvas { position: relative; width: 1200px; height: 1000px; }

  .card { position: absolute; left: 266px; width: 666px; height: 397px; overflow: hidden; box-shadow: 0 6px 14px rgba(0,0,0,.25); }
  .card--front { top: 74px; background: var(--ink); }
  .card--back { top: 533px; background: var(--ink); }

  .front__header { position: absolute; left: 0; top: 0; width: 100%; height: 194px; background: var(--paper); border-bottom: 4px solid var(--accent); }

  .brand { position: absolute; display: flex; flex-direction: column; align-items: center; }
  .brand__row { display: flex; align-items: center; gap: 10px; }
  .brand__square { width: 26px; height: 26px; }
  .brand__name { font-family: "Cinzel", serif; font-weight: 700; white-space: nowrap; }
  .brand__tagline { font-family: "Cinzel", serif; font-weight: 700; white-space: nowrap; }

  .brand--front { right: 32px; top: 98px; }
  .brand--front .brand__square { background: var(--accent); }
  .brand--front .brand__name { font-size: 25px; color: var(--ink); }
  .brand--front .brand__tagline { font-size: 10px; color: var(--accent); margin-top: 6px; }

  .brand--back { left: 0; right: 0; top: 180px; }
  .brand--back .brand__square { background: var(--paper); width: 40px; height: 40px; }
  .brand--back .brand__name { font-size: 34px; color: var(--paper); }
  .brand--back .brand__tagline { font-size: 13px; color: var(--paper); margin-top: 10px; }

  .portrait { position: absolute; left: 33px; top: 96px; width: 143px; height: 158px; border: 3px solid var(--paper); background: linear-gradient(160deg, var(--photo-mid), var(--photo-dark)); }

  .person { position: absolute; left: 32px; top: 276px; }
  .person__name { font-family: "Oswald", sans-serif; font-size: 19px; color: var(--accent); text-transform: uppercase; }
  .person__title { font-family: "Cinzel", serif; font-size: 14px; color: var(--text-light); margin-top: 2px; }

  .contact { position: absolute; left: 353px; top: 210px; font-family: "Open Sans", sans-serif; color: var(--text-light); font-size: 15.5px; line-height: 20px; }
  .contact__offices { display: flex; gap: 30px; margin-top: 8px; }
  .office__label { color: var(--accent); text-transform: uppercase; font-size: 15px; line-height: 20px; }
  .office__line { display: flex; align-items: center; gap: 5px; line-height: 21px; }
  .office__line svg { width: 14px; height: 12px; fill: var(--accent); }
  .contact__email { margin-top: 5px; }
  .contact__web { letter-spacing: 1px; margin-top: 3px; }
</style>
</head>
<body>
<div class="canvas">

  <section class="card card--front">
    <div class="front__header"></div>

    <div class="brand brand--front">
      <div class="brand__row">
        <span class="brand__square"></span>
        <span class="brand__name">MW Coverage Team, LLC.</span>
      </div>
      <span class="brand__tagline">Trusted Risk Advice For Homes And Businesses</span>
    </div>

    <div class="portrait" role="img" aria-label="Chest-up portrait photo of the president"></div>

    <div class="person">
      <p class="person__name">Tavish K. Merriam, CLCS</p>
      <p class="person__title">PRESIDENT &amp; CEO</p>
    </div>

    <div class="contact">
      <p>240 Harbor Crest Ln, Suite 12</p>
      <p>Linwood, GA 30999</p>
      <div class="contact__offices">
        <div class="office">
          <p class="office__label">Northgate</p>
          <p class="office__line"><svg viewBox="0 0 14 12"><path d="M1 4c0-2 3-3 6-3s6 1 6 3v1h-3V4H4v1H1zM3 6h8l2 5H1z"/></svg>555-014-2267</p>
          <p class="office__line"><svg viewBox="0 0 14 12"><path d="M3 0h8v3H3zM1 4h12v5h-2V7H3v2H1zM4 8h6v4H4z"/></svg>555-014-2268</p>
        </div>
        <div class="office">
          <p class="office__label">Pine Harbor</p>
          <p class="office__line"><svg viewBox="0 0 14 12"><path d="M1 4c0-2 3-3 6-3s6 1 6 3v1h-3V4H4v1H1zM3 6h8l2 5H1z"/></svg>555-014-2267</p>
          <p class="office__line"><svg viewBox="0 0 14 12"><path d="M3 0h8v3H3zM1 4h12v5h-2V7H3v2H1zM4 8h6v4H4z"/></svg>555-014-2268</p>
        </div>
      </div>
      <p class="contact__email">Tavish@mwcoverageteam.com</p>
      <p class="contact__web">www.mwcoverageteam.com</p>
    </div>
  </section>

  <section class="card card--back">
    <div class="brand brand--back">
      <div class="brand__row">
        <span class="brand__square"></span>
        <span class="brand__name">MW Coverage Team, LLC.</span>
      </div>
      <span class="brand__tagline">Trusted Risk Advice For Homes And Businesses</span>
    </div>
  </section>

</div>
</body>
</html>
```